Premium website for 'Kestrel Voyages Elite'

Exclusive Torque League travel packages: world-class tickets, premium hospitality, seamless travel, and curated experiences that bring the spirit of each destination to life.

1. Overall Style and Impression
Aesthetic: Modern, premium, and dynamic, reflecting the speed and excitement of a high-profile sport or event.

Focus: Highly visual and focused on driving users toward specific, high-value conversion points (like finding a race or viewing a premium package).

We need on the homepage a few blocks for all destinations.
One the specific page of the destination, we need a list of tickets.
An example for our website is https://zomerratours.com/

Functional requirements

The web site is designed to deliver an end-to-end Torque League travel experience, combining flight bookings, hotel reservations, and race ticket purchases into one seamless booking process. This system provides a unified API layer that integrates external booking services and enables developers to build, manage, and customize complete travel packages for each TL Grand Prix event.

System Overview

The platform is built around three core microservices, all connected through a central Package API:

1. Flight Booking Service ✈️
Integrates with global flight providers (e.g.,Flyvora API).

2. Hotel Booking Service 🏨
Connects to hotel aggregator APIs (e.g., Bunkly).
Offers real-time availability, dynamic pricing, and filtering by proximity to TL circuits.

3. Ticket Booking Service 🎟️
Manages TL race ticket inventory and seat categories (Grandstand, VIP, General Admission).

CUSTOMER FEEDBACK
After each booking, a customer will be asked to fill in a questionaire.

CHAT BOT
A chat bot will answer the frequently asked questions.

OUR VISION
We believe life is meant to be lived at full throttle.
Not just seen, but felt. Not just remembered, but relived again and again.

MISSION
That’s why we craft once-in-a-lifetime Torque League journeys — where the roar of the engines meets the soul of the city. Where luxury travel and local culture collide with pure adrenaline. Where you don’t just watch the race… you become part of its story.

PRODUCTS

Target Market(s)

Affluent individuals, typically 35−65 years old, in professional, executive, or entrepreneurial roles. High net worth with significant disposable income.

Coding

Coded - Design and coding required

Number of Pages Required

5+ page

Requirements
Must have
• Central Package API
Nice to have
• Customer feedback after each booking , chat bot.

```html
<!DOCTYPE html>
<html lang="en">
<head>
<meta charset="UTF-8">
<title>Kestrel Voyages Elite</title>
<link rel="stylesheet" href="https://fonts.googleapis.com/css2?family=Courier+Prime:wght@400;700&family=Montserrat:wght@400;500;600&display=swap">
<style>
:root{
  --red:#e00000;
  --black:#111111;
  --ink:#1a1a1a;
  --muted:#555555;
  --line:#c9c9c9;
  --pill:#fbe6e6;
  --grey-bg:#ebebeb;
  --white:#ffffff;
}
*{box-sizing:border-box;margin:0;padding:0}
html,body{width:1200px;height:3199px;overflow:hidden}
body{font-family:"Montserrat",sans-serif;color:var(--ink);background:var(--white);position:relative}

.site-header{height:86px;background:var(--black);display:flex;align-items:center;padding:0 60px;color:var(--white)}
.brand{font-family:"Courier Prime",monospace;font-weight:700;font-size:25px;letter-spacing:1px;text-transform:uppercase}
.main-nav{margin-left:auto;display:flex;gap:32px;align-items:center}
.main-nav a{color:var(--white);text-decoration:none;font-variant:small-caps;letter-spacing:.5px;font-size:15px}
.main-nav a.active{font-weight:600}
.btn-outline-light{margin-left:32px;border:1.5px solid var(--white);color:var(--white);padding:8px 16px;font-size:15px;text-decoration:none}

.hero{position:relative;height:497px;overflow:hidden}
.hero-photo{position:absolute;inset:0;background:linear-gradient(100deg,#2d2d2b 0%,#4b4d48 35%,#6e6a62 55%,#8a3a34 72%,#59524c 88%,#3e3b38 100%)}
.hero-content{position:relative;padding:100px 0 0 60px;color:var(--white)}
.hero-title{font-family:"Courier Prime",monospace;font-weight:700;font-size:50px;line-height:54px}
.hero-title span{display:block;font-weight:400}
.hero-text{margin-top:28px;width:400px;font-size:19px;line-height:27px}
.btn-red{display:inline-block;background:var(--red);color:var(--white);text-decoration:none;font-size:16px;padding:9px 16px}
.hero .btn-red{margin-top:30px;margin-left:1px}

.section-title{font-family:"Courier Prime",monospace;font-weight:700;font-size:41px;text-align:center;letter-spacing:.5px}
.section-title em{font-style:normal;color:var(--red)}
.title-bar{width:168px;height:4px;background:var(--red);margin:16px auto 0}

.destinations{padding:80px 0 0}
.card-grid{width:978px;margin:58px auto 0;display:grid;grid-template-columns:repeat(3,310px);column-gap:24px;row-gap:44px}
.race-card{border:1.5px solid var(--line);height:424px;background:var(--white)}
.race-card.featured{border-color:#f2a3a3;box-shadow:0 0 6px rgba(224,0,0,.25)}
.race-photo{height:216px}
.race-body{padding:22px 12px 0}
.date-pill{display:inline-block;background:var(--pill);border-radius:12px;font-size:11px;padding:4px 14px;margin-left:2px}
.date-pill sup{font-size:7px}
.race-name{font-size:18px;font-weight:500;margin-top:16px;white-space:nowrap}
.race-desc{font-size:12.5px;line-height:21px;color:var(--muted);margin-top:10px;padding-left:2px}
.btn-outline-red{display:inline-block;border:1.5px solid var(--red);color:var(--red);text-decoration:none;font-size:15px;padding:8px 17px;background:var(--white)}
.race-card .btn-outline-red,.race-card .btn-red{margin-top:13px;margin-left:1px}
.race-card .btn-red{font-size:15px;padding:9px 17px}
.view-more{text-align:center;margin-top:38px}
.view-more .btn-outline-red{padding:8px 15px}

.about{margin-top:86px;height:584px;background:var(--grey-bg);position:relative;overflow:hidden}
.about-inner{position:absolute;left:111px;top:86px;width:490px;z-index:1}
.about .section-title{text-align:left;white-space:nowrap;font-size:37px}
.about .title-bar{margin:16px 0 0;width:192px}
.about-text{font-size:15.5px;line-height:26px;color:#444;margin-top:40px}
.about-text+.about-text{margin-top:8px}
.about .btn-outline-red{margin-top:16px;padding:8px 12px}
.about-photo{position:absolute;left:632px;top:80px;width:512px;height:420px;background:radial-gradient(ellipse at 60% 60%,#d23a33 0%,#b32b26 30%,rgba(200,200,200,0) 68%)}

.testimonials{padding:80px 0 0}
.review-grid{width:978px;margin:58px auto 0;display:grid;grid-template-columns:repeat(3,310px);column-gap:24px}
.review-card{border:1.5px solid var(--line);height:214px;padding:28px 20px 0;position:relative}
.quote-mark{position:absolute;right:12px;top:12px}
.review-text{font-size:13px;line-height:21px;color:#444;margin-top:24px}
.reviewer{font-size:13px;font-weight:500;margin-top:14px}
.reviewer::before{content:"";display:inline-block;width:14px;height:1.5px;background:var(--red);vertical-align:middle;margin-right:10px}
.dots{display:flex;justify-content:center;gap:8px;margin-top:24px}
.dots span{width:10px;height:10px;border-radius:50%;background:#555}
.dots span.on{width:15px;height:15px;background:var(--red);margin-top:-2px}

.site-footer{position:absolute;top:2980px;left:0;width:1200px;height:219px;background:var(--black);color:var(--white);text-align:center}
.footer-brand{font-family:"Courier Prime",monospace;font-weight:700;font-size:36px;text-transform:uppercase;margin-top:52px;letter-spacing:1px}
.footer-nav{display:flex;justify-content:center;gap:46px;margin-top:22px}
.footer-nav a{color:var(--white);text-decoration:none;font-variant:small-caps;font-size:15px}
.footer-rule{height:1px;background:#444;margin-top:20px}
.copyright{font-size:13px;color:#ccc;margin-top:18px}
</style>
</head>
<body>

<header class="site-header">
  <div class="brand">Kestrel Voyages Elite</div>
  <nav class="main-nav">
    <a href="#" class="active">Home</a>
    <a href="#">Races</a>
    <a href="#">Packages</a>
    <a href="#">Experience</a>
    <a href="#">About</a>
    <a href="#">Contact</a>
  </nav>
  <a href="#" class="btn-outline-light">Book Now</a>
</header>

<section class="hero">
  <div class="hero-photo" role="img" aria-label="Red open-wheel race car speeding along a circuit, blurred cars and stands behind"></div>
  <div class="hero-content">
    <h1 class="hero-title">Exclusive Torque League<span>Travel Experiences</span></h1>
    <p class="hero-text">Luxury travel packages with VIP tickets, world-class hospitality, and seamless arrangements.</p>
    <a href="#" class="btn-red">View Packages</a>
  </div>
</section>

<section class="destinations">
  <h2 class="section-title"><em>Luxury TL</em> Destinations Await</h2>
  <div class="title-bar"></div>
  <div class="card-grid">
    <article class="race-card">
      <div class="race-photo" role="img" aria-label="Sports car wheel on a sunlit track" style="background:linear-gradient(160deg,#e7b878 0%,#9a7b63 40%,#3a3533 75%,#7b2a26 100%)"></div>
      <div class="race-body">
        <span class="date-pill">18<sup>th</sup> - 22<sup>th</sup>,Oct 2025</span>
        <h3 class="race-name">Rivena GP - Duis Aute Irure</h3>
        <p class="race-desc">Lorem ipsum dolor sit amet, consectetur ad ipiscing elit, sed do eiusmod</p>
        <a href="#" class="btn-outline-red">Book Now</a>
      </div>
    </article>
    <article class="race-card featured">
      <div class="race-photo" role="img" aria-label="Red sports car racing past a chequered flag" style="background:linear-gradient(150deg,#e9e6e1 0%,#b98460 35%,#c0311f 60%,#5a1a12 100%)"></div>
      <div class="race-body">
        <span class="date-pill">18<sup>th</sup> - 22<sup>th</sup>,Oct 2025</span>
        <h3 class="race-name">Solvara GP - Duis Aute</h3>
        <p class="race-desc">Lorem ipsum dolor sit amet, consectetur ad ipiscing elit, sed do eiusmod</p>
        <a href="#" class="btn-red">Book Now</a>
      </div>
    </article>
    <article class="race-card">
      <div class="race-photo" role="img" aria-label="Red race cars on a circuit at sunset" style="background:linear-gradient(170deg,#d9a978 0%,#8d7966 35%,#5b5552 60%,#a8312b 85%,#3a3432 100%)"></div>
      <div class="race-body">
        <span class="date-pill">18<sup>th</sup> - 22<sup>th</sup>,Oct 2025</span>
        <h3 class="race-name">Northfield GP - Duis Au</h3>
        <p class="race-desc">Lorem ipsum dolor sit amet, consectetur ad ipiscing elit, sed do eiusmod</p>
        <a href="#" class="btn-outline-red">Book Now</a>
      </div>
    </article>
    <article class="race-card">
      <div class="race-photo" role="img" aria-label="Row of sports cars lined up in the pit lane" style="background:linear-gradient(120deg,#6f8ba0 0%,#c0432e 35%,#e0a040 60%,#4d4d50 100%)"></div>
      <div class="race-body">
        <span class="date-pill">18<sup>th</sup> - 22<sup>th</sup>,Oct 2025</span>
        <h3 class="race-name">Qaran Dunes GP - Duis Aute</h3>
        <p class="race-desc">Lorem ipsum dolor sit amet, consectetur ad ipiscing elit, sed do eiusmod</p>
        <a href="#" class="btn-outline-red">Book Now</a>
      </div>
    </article>
    <article class="race-card">
      <div class="race-photo" role="img" aria-label="Dark open-wheel race cars side by side on track" style="background:linear-gradient(160deg,#2a2623 0%,#5c5046 40%,#b07a4e 70%,#5a3f2d 100%)"></div>
      <div class="race-body">
        <span class="date-pill">18<sup>th</sup> - 22<sup>th</sup>,Oct 2025</span>
        <h3 class="race-name">Marisport GP - Duis Aute</h3>
        <p class="race-desc">Lorem ipsum dolor sit amet, consectetur ad ipiscing elit, sed do eiusmod</p>
        <a href="#" class="btn-outline-red">Book Now</a>
      </div>
    </article>
    <article class="race-card">
      <div class="race-photo" role="img" aria-label="Race cars speeding on a blurred circuit" style="background:linear-gradient(170deg,#586a78 0%,#b34d35 35%,#4a4a4c 65%,#2c2c2e 100%)"></div>
      <div class="race-body">
        <span class="date-pill">18<sup>th</sup> - 22<sup>th</sup>,Oct 2025</span>
        <h3 class="race-name">Valdoria GP - Duis Aute Irure</h3>
        <p class="race-desc">Lorem ipsum dolor sit amet, consectetur ad ipiscing elit, sed do eiusmod</p>
        <a href="#" class="btn-outline-red">Book Now</a>
      </div>
    </article>
  </div>
  <div class="view-more"><a href="#" class="btn-outline-red">View More</a></div>
</section>

<section class="about">
  <div class="about-inner">
    <h2 class="section-title"><em>About</em> Kestrel Voyages Elite</h2>
    <div class="title-bar"></div>
    <p class="about-text">Lorem ipsum dolor sit amet, consectetur adipiscing elit, sed do eiusmod tempor incididunt ut labore et dolore magna aliqua. Ut enim ad minim veniam, quis nostrud exercitation ullamco laboris nisi ut aliquip ex ea commodo consequat. Duis aute irure dolor in reprehenderit in voluptate velit esse cillum dolore eu fugiat nulla pariatur. Excepteur sint occaecat cupidatat non proident, sunt in culpa qui officia</p>
    <p class="about-text">Sed ut perspiciatis unde omnis iste natus error sit voluptatem accusantium doloremque</p>
    <a href="#" class="btn-outline-red">Read More</a>
  </div>
  <div class="about-photo" role="img" aria-label="Driver in red race suit standing beside a red open-wheel race car"></div>
</section>

<section class="testimonials">
  <h2 class="section-title"><em>Our</em> TESTIMONIALS</h2>
  <div class="title-bar"></div>
  <div class="review-grid">
    <article class="review-card">
      <svg width="108" height="20" viewBox="0 0 108 20" aria-label="5 star rating"><g fill="#e00000"><path id="st" d="M10 1l2.6 6 6.4.5-4.9 4.2 1.5 6.3L10 14.6 4.4 18l1.5-6.3L1 7.5l6.4-.5z"/><use href="#st" x="21"/><use href="#st" x="42"/><use href="#st" x="63"/><use href="#st" x="84"/></g></svg>
      <svg class="quote-mark" width="78" height="48" viewBox="0 0 78 48"><g fill="#fbe3e3"><path d="M0 0h32v30l-14 18H6l10-18H0z"/><path d="M44 0h32v30l-14 18H50l10-18H44z"/></g></svg>
      <p class="review-text">“Sed ut perspiciatis unde omnis iste natus error sit voluptatem accusantium doloremque laudantium, totam rem aperiam, eaque ipsa quae ab illo”</p>
      <p class="reviewer">Alex R., Rivena GP</p>
    </article>
    <article class="review-card">
      <svg width="108" height="20" viewBox="0 0 108 20" aria-label="5 star rating"><g fill="#e00000"><use href="#st"/><use href="#st" x="21"/><use href="#st" x="42"/><use href="#st" x="63"/><use href="#st" x="84"/></g></svg>
      <svg class="quote-mark" width="78" height="48" viewBox="0 0 78 48"><g fill="#fbe3e3"><path d="M0 0h32v30l-14 18H6l10-18H0z"/><path d="M44 0h32v30l-14 18H50l10-18H44z"/></g></svg>
      <p class="review-text">“Sed ut perspiciatis unde omnis iste natus error sit voluptatem accusantium doloremque laudantium, totam rem aperiam, eaque ipsa quae ab illo”</p>
      <p class="reviewer">Alex R., Rivena GP</p>
    </article>
    <article class="review-card">
      <svg width="108" height="20" viewBox="0 0 108 20" aria-label="5 star rating"><g fill="#e00000"><use href="#st"/><use href="#st" x="21"/><use href="#st" x="42"/><use href="#st" x="63"/><use href="#st" x="84"/></g></svg>
      <svg class="quote-mark" width="78" height="48" viewBox="0 0 78 48"><g fill="#fbe3e3"><path d="M0 0h32v30l-14 18H6l10-18H0z"/><path d="M44 0h32v30l-14 18H50l10-18H44z"/></g></svg>
      <p class="review-text">“Sed ut perspiciatis unde omnis iste natus error sit voluptatem accusantium doloremque laudantium, totam rem aperiam, eaque ipsa quae ab illo”</p>
      <p class="reviewer">Alex R., Rivena GP</p>
    </article>
  </div>
  <div class="dots"><span class="on"></span><span></span><span></span><span></span></div>
</section>

<footer class="site-footer">
  <div class="footer-brand">Kestrel Voyages Elite</div>
  <nav class="footer-nav">
    <a href="#">Home</a><a href="#">Races</a><a href="#">Packages</a><a href="#">Experience</a><a href="#">About</a><a href="#">Contact</a>
  </nav>
  <div class="footer-rule"></div>
  <p class="copyright">Copyright © 2025 Kestrel Voyages Elite. All rights reserved.</p>
</footer>

</body>
</html>
```